I'm looking for a book cover with the Main title:
Where the Lanterns Drift Beyond the Harbour Mist at Dusk

Subtitle: A Wanderer's Chronicle of Salt and Ember

Looking for a clean design that attracts people to the book.

Open to all styles of design (plain text, animated characters, scenery) as long as the text is in basic font and easy to read.

This is to be put somewhere under the titles
Written By: Bogumil Trenkaro

The back of the book will have:

"A physical, mental, emotional, and spiritual guide to fat loss. Going beyond calorie deficit diets and working out for hours a day in order to achieve results. It will help you get to the root cause of weight gain and give you the tools you need to take charge of your health and your life.

You will learn:
- The Best Foods to Eat for Fat Loss
- The Foods You Need to Avoid
- How to Heal Your Hormones
- Strategies to Overcome Emotional Eating
- Mindset and Motivation Tactics
- How to Meditate Without Losing Your Mind

I created this book to help those struggling with losing fat in a healthy, holistic, and sustainable way. It’s my sincere hope that this book gives you what you need in order to achieve your goals. "

Please place the photo somewhere on the back as well if it fits with the design.

Thank you for your time!

```html
<!DOCTYPE html>
<html lang="en">
<head>
<meta charset="utf-8">
<title>Where the Lanterns Drift Beyond the Harbour Mist at Dusk — Bogumil Trenkaro</title>
<link rel="stylesheet" href="https://fonts.googleapis.com/css2?family=Montserrat:wght@200;300;700;800&display=swap">
<style>
  :root {
    --paper: #e8e8e8;
    --sky: #55b3df;
    --rose: #cc2a6a;
    --chalk: #ebebeb;
  }
  html, body {
    margin: 0;
    padding: 0;
    overflow: hidden;
    background: var(--paper);
  }
  .cover {
    display: block;
    width: 802px;
    height: 1200px;
    background: var(--paper);
  }
  .cover text {
    font-family: "Montserrat", "Helvetica Neue", Arial, sans-serif;
  }
  .panel { fill: var(--sky); }
  .title-light { fill: var(--chalk); font-weight: 800; }
  .title-accent { fill: var(--rose); font-weight: 800; }
  .title-accent .thin { font-weight: 200; }
  .subtitle { fill: var(--rose); font-weight: 800; font-size: 27px; }
  .author { fill: var(--sky); font-weight: 200; font-size: 56px; }
</style>
</head>
<body>
<svg class="cover" viewBox="0 0 802 1200" width="802" height="1200" xmlns="http://www.w3.org/2000/svg">
  <defs>
    <clipPath id="panel-clip">
      <path d="M0 0 H705 V1049 Q705 1066 688 1066 H0 Z"/>
    </clipPath>
  </defs>

  <path class="panel" d="M0 0 H705 V1049 Q705 1066 688 1066 H0 Z"/>

  <g class="title" clip-path="url(#panel-clip)">
    <text class="title-light" x="0" y="92" font-size="124" textLength="545" lengthAdjust="spacingAndGlyphs">WHERE THE</text>

    <text class="title-accent" x="0" y="236" font-size="156" textLength="662" lengthAdjust="spacingAndGlyphs">LAN<tspan class="thin">TERNS</tspan></text>
    <text class="title-accent" x="0" y="376" font-size="141">DRIFT</text>

    <text class="title-light" x="0" y="514" font-size="141" textLength="640" lengthAdjust="spacingAndGlyphs">BEYOND</text>
    <text class="title-light" x="0" y="654" font-size="141">THE</text>
    <text class="title-light" x="0" y="791" font-size="141" textLength="712" lengthAdjust="spacingAndGlyphs">HARBOUR</text>
    <text class="title-light" x="0" y="931" font-size="141" textLength="640" lengthAdjust="spacingAndGlyphs">MIST AT</text>
    <text class="title-light" x="0" y="1070" font-size="141">DUSK</text>
  </g>

  <text class="subtitle" x="12" y="1114" textLength="690" lengthAdjust="spacingAndGlyphs">A WANDERER'S CHRONICLE OF SALT AND EMBER</text>
  <text class="author" x="7" y="1182" textLength="693" lengthAdjust="spacing">BOGUMIL TRENKARO</text>
</svg>
</body>
</html>
```